Organic skincare label - minimalist, earthy, luxe design needed!

I need a label design for a luxury natural skin care line called "Velka Botanix". Velka means 'earth' in Swahili. I would like the design to embody an earthy feel but be minimalistic and give a luxe vibe. My first product will be a Tumeric and Neem Scrub.

The size of the jar is 8oz, label dimensions should be (1.625" Tall x 8.5" Wide)
I will be making other products too such as; oils + toners so I feel free to do labels for glass bottles and/or spray bottles as well.

Forest green, light pinks/nudes/beige, grey, white, gold, are colors that can be used (not all have to be used).

I have included pictures of some things I've worked on myself as well as my original logo design but I need to simplify the logo, no circle around it.
Feel free to get creative.

Thank you! :)
Updates

Target Market(s)

Socially Conscious, Beauty Enthusiast, Minimalist

Industry/Entity Type

Skin Care

Font styles to use
Sans Serif
Other font styles liked:
• "Wonderlove doodle" is the font used for "Velka" in the logo. Feel free to use that or change it as you see fit.

Requirements
Must have
• Simplistic design
would like to stick to a font close to the ones in the logo. Either the one used for the name "Velka" OR the one that the slogan "rooted tonics" uses.

I have also included some pictures to capture the aesthetic of my social media and website.

Gender neutral

```html
<!DOCTYPE html>
<html lang="en">
<head>
<meta charset="utf-8">
<title>Velka Botanix – Tumeric and Neem Scrub labels</title>
<link rel="stylesheet" href="https://fonts.googleapis.com/css2?family=Marcellus+SC&family=Open+Sans:wght@400;700&display=swap">
<style>
  :root {
    --page: #eef8fb;
    --brown: #7b4a2a;
    --tan: #d5b696;
    --sand: #e8dcb3;
    --cream: #f8eedc;
    --white: #ffffff;
    --tan-light: #d8bc9c;
  }
  * { box-sizing: border-box; margin: 0; padding: 0; }
  html, body { width: 1167px; height: 1200px; overflow: hidden; }
  body {
    background: var(--page);
    font-family: "Open Sans", sans-serif;
    position: relative;
  }
  .label {
    position: absolute;
    left: 88px;
    width: 992px;
    height: 189px;
    overflow: hidden;
    box-shadow: 0 2px 6px rgba(120, 90, 60, 0.15);
  }
  .label--tan { top: 256px; background: var(--tan); color: var(--cream); }
  .label--sand { top: 505px; background: var(--sand); color: var(--brown); }
  .label--white { top: 754px; background: var(--white); color: var(--brown); }

  .globe {
    position: absolute;
    left: 200px; top: -20px;
    width: 252px; height: 229px;
    border-radius: 50%;
  }
  .label--tan .globe { background: radial-gradient(circle, rgba(243,231,207,0.55), rgba(243,231,207,0.15) 70%, transparent 72%); }
  .label--sand .globe { background: radial-gradient(circle, rgba(255,250,235,0.6), rgba(255,250,235,0.2) 70%, transparent 72%); }
  .label--white .globe { background: radial-gradient(circle, rgba(201,165,127,0.45), rgba(201,165,127,0.12) 70%, transparent 72%); }

  .brand { position: absolute; text-align: center; }
  .brand__name { font-weight: 700; letter-spacing: 0.5px; line-height: 1; }
  .brand__tagline { font-weight: 400; letter-spacing: 0.4px; white-space: nowrap; }

  .brand--main { left: 473px; top: 68px; width: 160px; }
  .brand--main .brand__name { font-size: 40px; }
  .brand--main .brand__tagline { font-size: 11px; margin-top: 2px; }

  .brand--side { left: 725px; top: 48px; width: 120px; }
  .brand--side .brand__name { font-size: 28px; }
  .brand--side .brand__tagline { font-size: 9.5px; margin-top: 2px; }

  .label--tan .brand__name { color: var(--cream); }
  .label--sand .brand__name { color: var(--brown); }
  .label--white .brand--main .brand__name { color: var(--brown); }
  .label--white .brand--side .brand__name,
  .label--white .brand--side .brand__tagline { color: var(--tan-light); }

  .product-title {
    position: absolute;
    left: 447px; top: 140px;
    font-family: "Marcellus SC", serif;
    font-size: 21px;
    letter-spacing: 0.6px;
    white-space: nowrap;
  }

  .ingredients {
    position: absolute;
    left: 734px; top: 101px;
    width: 240px;
    font-size: 7.9px;
    line-height: 9.8px;
  }
  .ingredients__heading { font-weight: 700; font-size: 8.6px; }
  .label--white .ingredients { color: var(--tan-light); }

  .maker {
    position: absolute;
    left: 28px; top: 151px;
    display: flex; align-items: flex-end; gap: 12px;
  }
  .maker__mark { font-weight: 700; font-size: 13px; line-height: 1; color: var(--brown); }
  .maker__text { font-size: 8px; line-height: 9.5px; color: var(--brown); }
  .maker__name { font-weight: 700; }
</style>
</head>
<body>

  <section class="label label--tan">
    <div class="globe" role="img" aria-label="Line-network world globe illustration centred on Africa"></div>
    <div class="brand brand--main"><p class="brand__name">Velka</p><p class="brand__tagline">rooted tonics</p></div>
    <p class="product-title">Tumeric and Neem Scrub</p>
    <div class="brand brand--side"><p class="brand__name">Velka</p><p class="brand__tagline">rooted tonics</p></div>
    <div class="ingredients">
      <p class="ingredients__heading">Ingredients</p>
      <p>Just a sample of ingredients, Panthenol, Polyglyceryl-10 Laurate, Polyglyceryl-10 Myristate, Glycerine, Arginine, Allantoin, Asiaticoside, Asiatic acid, Madecassic acid, Sodium Hyaluronate, Gardenia Florida Fruit Extract, Citrus Aurantium Bergamia (Bergamot) Fruit Oil, Menthyl Lactate, Mentha Haplocalix Extract</p>
    </div>
    <div class="maker">
      <span class="maker__mark">Velka</span>
      <p class="maker__text">Crafted by:<br><span class="maker__name">Velka Botanix</span><br>bla-bla-bla 12345 bla bla bla</p>
    </div>
  </section>

  <section class="label label--sand">
    <div class="globe" role="img" aria-label="Line-network world globe illustration centred on Africa"></div>
    <div class="brand brand--main"><p class="brand__name">Velka</p><p class="brand__tagline">rooted tonics</p></div>
    <p class="product-title">Tumeric and Neem Scrub</p>
    <div class="brand brand--side"><p class="brand__name">Velka</p><p class="brand__tagline">rooted tonics</p></div>
    <div class="ingredients">
      <p class="ingredients__heading">Ingredients</p>
      <p>Just a sample of ingredients, Panthenol, Polyglyceryl-10 Laurate, Polyglyceryl-10 Myristate, Glycerine, Arginine, Allantoin, Asiaticoside, Asiatic acid, Madecassic acid, Sodium Hyaluronate, Gardenia Florida Fruit Extract, Citrus Aurantium Bergamia (Bergamot) Fruit Oil, Menthyl Lactate, Mentha Haplocalix Extract</p>
    </div>
    <div class="maker">
      <span class="maker__mark">Velka</span>
      <p class="maker__text">Crafted by:<br><span class="maker__name">Velka Botanix</span><br>bla-bla-bla 12345 bla bla bla</p>
    </div>
  </section>

  <section class="label label--white">
    <div class="globe" role="img" aria-label="Line-network world globe illustration centred on Africa"></div>
    <div class="brand brand--main"><p class="brand__name">Velka</p><p class="brand__tagline">rooted tonics</p></div>
    <p class="product-title">Tumeric and Neem Scrub</p>
    <div class="brand brand--side"><p class="brand__name">Velka</p><p class="brand__tagline">rooted tonics</p></div>
    <div class="ingredients">
      <p class="ingredients__heading">Ingredients</p>
      <p>Just a sample of ingredients, Panthenol, Polyglyceryl-10 Laurate, Polyglyceryl-10 Myristate, Glycerine, Arginine, Allantoin, Asiaticoside, Asiatic acid, Madecassic acid, Sodium Hyaluronate, Gardenia Florida Fruit Extract, Citrus Aurantium Bergamia (Bergamot) Fruit Oil, Menthyl Lactate, Mentha Haplocalix Extract</p>
    </div>
    <div class="maker">
      <span class="maker__mark">Velka</span>
      <p class="maker__text">Crafted by:<br><span class="maker__name">Velka Botanix</span><br>bla-bla-bla 12345 bla bla bla</p>
    </div>
  </section>

</body>
</html>
```